Kessalt Orthodontics
Stationary, Business Card, Appointment Card, Envelope, Folder
Project: Kessalt Orthodontics
Kessalt Orthodontics - Health
Creative Brief
Professional
Marcus Kessalt, DMD
4183 Harlow Crest Dr., #210 Sacramento, CA 95871 6452 Bramwell-Tusk Rd., #B Elk Grove, CA 95683
info@kessaltortho-example.com
www.kessaltortho-example.com
Looking for letterhead, envelopes, business card, presentation folder
Would like a map of the two office locations in relation to each other. Have a business card with a map image if needed.

```html
<!DOCTYPE html>
<html lang="en">
<head>
<meta charset="utf-8">
<title>Kessalt Orthodontics – Business Card</title>
<link rel="stylesheet" href="https://fonts.googleapis.com/css2?family=Libre+Baskerville:wght@400;700&display=swap">
<style>
  :root {
    --backdrop: #ddd6cb;
    --card-white: #ffffff;
    --navy: #142553;
    --accent-blue: #3aa6dc;
    --ink: #2a2f3f;
    --faint: #e6e9f0;
    --map-light: #ece8df;
    --map-mid: #d9d4c8;
  }
  * { margin: 0; padding: 0; box-sizing: border-box; }
  html, body { width: 1200px; height: 959px; overflow: hidden; }
  body {
    background: var(--backdrop);
    font-family: "Libre Baskerville", "Times New Roman", serif;
    position: relative;
  }
  .card {
    position: absolute;
    top: 75px;
    width: 470px;
    height: 812px;
    box-shadow: 0 6px 18px rgba(0,0,0,0.28);
  }
  .card--front { left: 100px; background: var(--card-white); color: var(--navy); }
  .card--back { left: 630px; background: var(--navy); color: #fff; }

  .brand {
    position: absolute;
    left: 0; right: 0;
    top: 48px;
    display: flex;
    align-items: center;
    justify-content: center;
    gap: 14px;
  }
  .card--back .brand { top: 34px; }
  .brand__mark {
    width: 26px; height: 26px;
    border-radius: 50%;
    background: var(--accent-blue);
    flex: none;
  }
  .brand__name {
    font-size: 30px;
    font-weight: 700;
    line-height: 1.05;
    text-align: left;
  }
  .card--front .brand__name { color: var(--navy); }
  .card--back .brand__name { color: #fff; }
  .brand__name small { display: block; font-size: 17px; letter-spacing: 1px; }

  .doctor-line {
    position: absolute;
    left: 0; right: 0;
    top: 146px;
    text-align: center;
    font-size: 13px;
    font-weight: 700;
    letter-spacing: 6px;
  }
  .card--back .doctor-line { top: 112px; }
  .rule {
    position: absolute;
    left: 40px; right: 40px;
    height: 3px;
    background: var(--accent-blue);
  }
  .rule--top { top: 132px; }
  .rule--bottom { top: 742px; }

  .watermark {
    position: absolute;
    left: 125px; top: 185px;
    width: 220px; height: 220px;
    border-radius: 50%;
    background: var(--faint);
  }

  .contact {
    position: absolute;
    left: 40px; top: 440px;
    color: var(--ink);
    font-size: 15px;
    line-height: 1.5;
  }
  .contact__name {
    font-size: 22px;
    font-weight: 700;
    color: var(--navy);
    margin-bottom: 14px;
    letter-spacing: 0.5px;
  }
  .contact__block { margin-bottom: 14px; }
  .contact__web { font-size: 16px; }

  .map {
    position: absolute;
    left: 28px; right: 28px;
    background: linear-gradient(135deg, var(--map-light), var(--map-mid));
    border: 2px solid #fff;
  }
  .map--sacramento { top: 156px; height: 228px; }
  .map--elk-grove { top: 545px; height: 240px; }

  .locations {
    position: absolute;
    left: 40px; right: 20px;
    top: 405px;
    font-size: 16px;
    font-weight: 700;
    line-height: 1.45;
  }
  .locations p { margin-bottom: 14px; }
</style>
</head>
<body>
  <section class="card card--front" aria-label="Business card front">
    <div class="brand">
      <span class="brand__mark"></span>
      <div class="brand__name">Kessalt<small>ORTHODONTICS</small></div>
    </div>
    <div class="rule rule--top"></div>
    <div class="doctor-line">MARCUS KESSALT, DMD</div>
    <div class="watermark"></div>
    <div class="contact">
      <div class="contact__name">MARCUS KESSALT, DMD</div>
      <div class="contact__block">P: (916) 555-0142<br>E: info@kessaltortho-example.com</div>
      <div class="contact__block">4183 Harlow Crest Dr., #210<br>Sacramento, CA 95871</div>
      <div class="contact__block">6452 Bramwell-Tusk Rd., #B<br>Elk Grove, CA 95683</div>
      <div class="contact__web">www.kessaltortho-example.com</div>
    </div>
    <div class="rule rule--bottom"></div>
  </section>

  <section class="card card--back" aria-label="Business card back">
    <div class="brand">
      <span class="brand__mark"></span>
      <div class="brand__name">Kessalt<small>ORTHODONTICS</small></div>
    </div>
    <div class="doctor-line">MARCUS KESSALT, DMD</div>
    <div class="map map--sacramento" role="img" aria-label="Street map showing the Sacramento office location"></div>
    <div class="locations">
      <p>4183 Harlow Crest Dr., #210<br>Sacramento, CA 95871</p>
      <p>6452 Bramwell-Tusk Rd., #B<br>Elk Grove, CA 95683</p>
    </div>
    <div class="map map--elk-grove" role="img" aria-label="Street map showing the Elk Grove office location"></div>
  </section>
</body>
</html>
```